ONE PAGE WEB DESIGN NEEDED for Finance Company

We need a web design (ONE PAGE DESIGN ONLY) for a new finance website called Corvella Lending. Corvella Lending helps customers get the right loan, whether its a home loan, investment loan, business loan etc.

You are required to come up with just the homepage design. Professionalism and quality is the key factors in the successful design.

Here are a few design questions to help you out:

-
What information should be used on the page?
Ive provided a document which outlines all the information needed to put on homepage (attached to the brief - called corvella_page_info). Also see the Must Have section below on this brief.

-
What links should appear in the navigation/footer?:
The navigation should provide links to the following pages (NOTE: services link has subcategories):
1 Homepage
2 Services
- Home loans
- Investment loans
- Refinancing loans
- Business loans
3 About Us
4 FAQ
5 Contact Us

-
What colors should be used in the design?
Our company colors - Cyan: #2EADE3, Blue: #004B70, White. Feel free to submit designs with slight variations if you feel it improves the design.

-
What should the layout of the page be?
This is up to you to come up with - we are open to different layouts for the page design (as long as they capture the information effectively and making it easy to understand).

Target Market(s)

Potential Home owners, Families and Business Owners

Industry/Entity Type

Business

Requirements
Must have
• - Must contain our logo (attached as PNG and Illustrator file)
- Winning designer must supply a Photoshop file (PSD) that will allow us.
Nice to have
• - Should include photos/images of families, professional groups, tradespeople etc (you can use stock photos from PixelVaultImages and I will purchase them once you are selected as the winning design)
- Link to a loan calculator somewhere on front page with a button 'Find out how much you could borrow' (or maybe even try adding a loan calculator to the homepage if you think this would look good)
- Page should have a main headline "Finding the right loan for you" or "Corvella Lending finds the right loan for our customers."
- Must include Accreditation logos somewhere on the homepage (will try and supply these soon)
Should not have
• - Poor quality designs will not be considered
- Do not use clipart

```html
<!DOCTYPE html>
<html lang="en">
<head>
<meta charset="utf-8">
<title>Corvella Lending – Home</title>
<link href="https://fonts.googleapis.com/css2?family=Arimo:wght@400;700&family=Open+Sans:wght@400;600&family=Roboto+Condensed:wght@300&display=swap" rel="stylesheet">
<style>
:root{
  --cyan:#2eade3;
  --blue:#004b70;
  --white:#fff;
  --ink:#222;
  --grey:#555;
}
*{margin:0;padding:0;box-sizing:border-box}
html,body{width:1200px;height:1200px;overflow:hidden;background:var(--white)}
body{position:relative;font-family:"Arimo",Arial,sans-serif;color:var(--ink)}
a{text-decoration:none}
.abs{position:absolute}

.brand{left:130px;top:46px;display:flex;align-items:center;gap:8px}
.brand-square{width:14px;height:14px;background:var(--cyan)}
.brand-name{font-size:17px;font-weight:700;color:var(--blue)}

.main-nav{right:130px;top:54px;display:flex;gap:39px;font-size:14px;font-weight:700}
.main-nav a{color:var(--cyan)}
.main-nav a.current{color:var(--blue)}

.sub-band{left:0;top:80px;width:1200px;height:40px;background:var(--cyan);box-shadow:inset 0 3px 3px rgba(0,0,0,.12)}
.nav-pointer{left:754px;top:80px;width:0;height:0;border-left:5px solid transparent;border-right:5px solid transparent;border-top:5px solid var(--white)}
.sub-nav{right:130px;top:94px;display:flex;gap:17px;font-size:12px;color:var(--white)}

.hero{left:0;top:120px;width:1200px;height:280px;background:linear-gradient(180deg,#c98a5a 0%,#e8b27a 30%,#b27a4e 62%,#5a3a24 100%)}
.hero-title{left:0;top:160px;width:570px;height:110px;background:var(--blue);padding:8px 0 0 128px;font-family:"Roboto Condensed",Arial,sans-serif;font-weight:300;font-size:37px;line-height:43px;color:var(--white)}
.hero-arrow{top:275px;width:40px;height:40px;background:rgba(0,75,112,.85);display:flex;align-items:center;justify-content:center}

.intro{left:130px;top:438px;width:615px;font-size:12px;line-height:14px}
.intro p{margin-bottom:8px}
.hl{color:var(--cyan);font-weight:700}
.calc-link{left:770px;top:440px;display:flex;align-items:center;gap:20px}
.calc-ring{width:58px;height:58px;border-radius:50%;border:2px solid var(--cyan);display:flex;align-items:center;justify-content:center}
.calc-text{font-size:14px;font-weight:700;color:var(--cyan);line-height:17px;width:210px}

.service{top:570px;width:240px;text-align:center}
.service-icon{width:60px;height:60px;border-radius:50%;background:var(--cyan);margin:0 auto;display:flex;align-items:center;justify-content:center}
.service h3{font-family:"Open Sans",Arial,sans-serif;font-weight:400;font-size:19px;color:var(--blue);margin:6px 0 8px}
.service h4{font-size:12px;font-weight:700;color:var(--blue);margin-bottom:7px}
.service p{font-size:12px;line-height:14px;padding:0 8px}
.service p.narrow{padding:0 22px}

.divider{left:130px;top:750px;width:940px;border-top:1px dotted var(--cyan)}
.panel-copy{left:130px;top:778px;width:620px;font-size:12px;line-height:14px}
.panel-copy p{margin-bottom:7px}
.accred-title{left:770px;top:778px;font-size:12px;font-weight:700;color:var(--cyan)}
.partner{top:814px;width:62px;height:24px;background:#d6d6d6;border-radius:3px}

.footer-rule{left:130px;top:919px;width:940px;border-top:2px solid var(--cyan)}
.footer-links{left:130px;top:934px;font-size:11px;line-height:20px}
.social{top:940px;width:25px;height:25px;border-radius:50%;background:var(--cyan)}
</style>
</head>
<body>
<header>
  <div class="abs brand"><span class="brand-square"></span><span class="brand-name">Corvella Lending</span></div>
  <nav class="abs main-nav">
    <a class="current" href="#">Home</a><a href="#">Services</a><a href="#">About Us</a><a href="#">FAQ</a><a href="#">Contact Us</a>
  </nav>
  <div class="abs sub-band"></div>
  <div class="abs nav-pointer"></div>
  <nav class="abs sub-nav"><span>&gt; Home loans</span><span>&gt; Investment loans</span><span>&gt; Refinancing loans</span><span>&gt; Business loans</span></nav>
</header>

<section>
  <div class="abs hero" role="img" aria-label="Family with bicycles beside a car on the beach at sunset"></div>
  <h1 class="abs hero-title">Corvella Lending finds the right loan for our customers.</h1>
  <div class="abs hero-arrow" style="left:130px"><svg width="14" height="22"><path d="M11 2 3 11l8 9" fill="none" stroke="#fff" stroke-width="2.5"/></svg></div>
  <div class="abs hero-arrow" style="left:175px"><svg width="14" height="22"><path d="M3 2l8 9-8 9" fill="none" stroke="#fff" stroke-width="2.5"/></svg></div>
</section>

<section>
  <div class="abs intro">
    <p>At <span class="hl">Corvella Lending</span> we work hard to find the right loan for our customers. We do that because we are backed by sound industry knowledge, professional experience and a great customer service approach. Corvella Lending guarantees that we will always tailor the best solution for your individual lending needs.</p>
    <p>We can do that because we have access to a wide variety of lending options from major banks to non-bank lenders and we are committed to finding the right lending product for you.</p>
    <p class="hl">We offer a unique approach to help you find the right:</p>
  </div>
  <a class="abs calc-link" href="#">
    <span class="calc-ring"><svg width="20" height="26"><rect x="1" y="1" width="18" height="24" rx="2" fill="none" stroke="#2eade3" stroke-width="2"/><rect x="4" y="4" width="12" height="5" fill="#2eade3"/><g fill="#2eade3"><rect x="4" y="12" width="3" height="3"/><rect x="8.5" y="12" width="3" height="3"/><rect x="13" y="12" width="3" height="3"/><rect x="4" y="17" width="3" height="3"/><rect x="8.5" y="17" width="3" height="3"/><rect x="13" y="17" width="3" height="3"/></g></svg></span>
    <span class="calc-text">Find out how much you could borrow &nbsp;<svg width="14" height="11"><path d="M1 1l5 4.5L1 10M7 1l5 4.5L7 10" fill="none" stroke="#2eade3" stroke-width="2.2"/></svg></span>
  </a>

  <div class="abs service" style="left:120px">
    <div class="service-icon"><svg width="26" height="22"><path d="M2 12 11 4l9 8v8H2z" fill="#fff"/><circle cx="19" cy="8" r="6" fill="#fff" stroke="#2eade3" stroke-width="1.5"/><text x="19" y="11" font-size="9" font-weight="700" text-anchor="middle" fill="#2eade3" font-family="Arimo">$</text></svg></div>
    <h3>Home Loan</h3>
    <p class="narrow">Home buyers, First home buyers, Over 20 lenders</p>
  </div>
  <div class="abs service" style="left:360px">
    <div class="service-icon"><svg width="26" height="16"><g fill="#fff"><rect x="0" y="4" width="9" height="2"/><rect x="0" y="8" width="9" height="2"/><rect x="0" y="12" width="9" height="2"/><rect x="11" y="2" width="8" height="3"/><rect x="11" y="7" width="8" height="3"/><rect x="11" y="12" width="8" height="3"/><rect x="21" y="7" width="5" height="3"/><rect x="21" y="12" width="5" height="3"/></g></svg></div>
    <h3>Investment Loan</h3>
    <p>Property investment loans, Interest only loans</p>
  </div>
  <div class="abs service" style="left:600px">
    <div class="service-icon"><svg width="26" height="24"><g fill="#fff"><rect x="2" y="16" width="3" height="7"/><rect x="7" y="13" width="3" height="10"/><rect x="12" y="10" width="3" height="13"/><rect x="17" y="7" width="3" height="16"/></g><path d="M2 12 9 7l5 3 9-8" fill="none" stroke="#fff" stroke-width="2"/><path d="M18 1h6v6z" fill="#fff"/></svg></div>
    <h3>Refinancing</h3>
    <p>Refinancing for the best rate, Upsizing or downsizing, Change from a variable to a fixed rate</p>
  </div>
  <div class="abs service" style="left:840px">
    <div class="service-icon"><svg width="26" height="22"><path d="M2 12 11 4l9 8v8H2z" fill="#fff"/><circle cx="19" cy="8" r="6" fill="#fff" stroke="#2eade3" stroke-width="1.5"/><text x="19" y="11" font-size="9" font-weight="700" text-anchor="middle" fill="#2eade3" font-family="Arimo">$</text></svg></div>
    <h3>BusinessLoan</h3>
    <h4>Business Finance</h4>
    <p>Long term, Short term, Equipment and Leasing</p>
  </div>

  <div class="abs divider"></div>

  <div class="abs panel-copy">
    <p>There are many different loan products in the marketplace. Corvella Lending has access to a wide panel of lenders which means we can access bank and non-bank lenders that meet the individual needs of our customers.</p>
    <p class="hl">Contact Corvella Lending today on: 1800 246 810 to find out more.</p>
  </div>
  <div class="abs accred-title">Accreditation logos</div>
  <div class="abs partner" style="left:770px;width:98px" role="img" aria-label="Accreditation badge"></div>
  <div class="abs partner" style="left:930px;width:98px" role="img" aria-label="Accreditation badge"></div>
</section>

<footer>
  <div class="abs footer-rule"></div>
  <div class="abs footer-links">
    <div>Terms of Use | Legal notice | Sitemap | Disclaimer</div>
    <div>Copyright © 2012 Corvella Lending.&nbsp; All rights reserved.</div>
  </div>
  <span class="abs social" style="left:930px" aria-label="Social link"></span>
  <span class="abs social" style="left:969px" aria-label="Social link"></span>
  <span class="abs social" style="left:1007px" aria-label="Social link"></span>
  <span class="abs social" style="left:1045px" aria-label="Social link"></span>
</footer>
</body>
</html>
```